Business Card Design

I'm a commercial general contractor remodel offices, hotels, health clubs and stores mostly San Francisco and the peninsula
the file I down loaded is kind of what I want I like the I beam with my company name in it, that would be fine with me but if you have better Idea will look at it you never know, I'm decided to give in and change my company name to how every one knows me, I have been in business since 1991, I like the I beam logo I included one of my old card from my old company for reference for you.

Industry/Entity Type

Business

Contact Information for Business Card

BRAXO CONSTRUCTION (is my company name)
Wendell Trusk contractor, LIc 314827
4158 Garnet Row, San Bruno, California 94066
mobile, (415) 555-0147
phone (650) 555-0182
Fax, (650) 555-0183
email, braxo@braxoconstruction.example

```html
<!DOCTYPE html>
<html lang="en">
<head>
<meta charset="utf-8">
<title>Braxo Construction – Business Card</title>
<link rel="stylesheet" href="https://fonts.googleapis.com/css2?family=Nunito:wght@800;900&family=Arimo:wght@700&display=swap">
<style>
  :root {
    --card-bg: #ffffff;
    --brand-blue: #1c9ddf;
    --ink: #1a1a1a;
    --mark-grey: #4a4a4a;
    --name-shadow: rgba(0, 0, 0, 0.28);
  }
  * { margin: 0; padding: 0; box-sizing: border-box; }
  html, body {
    width: 1200px;
    height: 705px;
    overflow: hidden;
    background: var(--card-bg);
  }
  .card {
    position: relative;
    width: 1200px;
    height: 705px;
    background: var(--card-bg);
    font-family: "Arimo", Arial, sans-serif;
    font-weight: 700;
    color: var(--ink);
  }
  .brand {
    position: absolute;
    left: 70px;
    top: 150px;
    display: flex;
    align-items: center;
    gap: 22px;
  }
  .brand-square {
    width: 64px;
    height: 64px;
    background: var(--mark-grey);
  }
  .brand-name {
    font-family: "Nunito", Arial, sans-serif;
    font-weight: 900;
    font-size: 46px;
    letter-spacing: 1px;
    color: var(--brand-blue);
  }
  .license {
    position: absolute;
    left: 736px;
    top: 73px;
    width: 413px;
    height: 71px;
    border: 4px solid var(--ink);
    border-radius: 22px;
    display: flex;
    align-items: center;
    justify-content: center;
    font-size: 44px;
  }
  .email {
    position: absolute;
    right: 51px;
    top: 286px;
    font-size: 30px;
  }
  .contractor-name {
    position: absolute;
    left: 44px;
    top: 398px;
    font-family: "Nunito", Arial, sans-serif;
    font-weight: 900;
    font-size: 86px;
    line-height: 1;
    color: var(--brand-blue);
    text-shadow: 3px 4px 4px var(--name-shadow);
    white-space: nowrap;
  }
  .phones {
    position: absolute;
    left: 44px;
    top: 520px;
    font-size: 31px;
    line-height: 58px;
  }
  .phones .row { display: flex; }
  .phones .label { width: 144px; }
  .address {
    position: absolute;
    right: 105px;
    top: 565px;
    text-align: center;
    font-size: 31px;
    line-height: 58px;
  }
</style>
</head>
<body>
  <main class="card">
    <div class="brand">
      <span class="brand-square"></span>
      <span class="brand-name">BRAXO CONSTRUCTION</span>
    </div>

    <div class="license">Lic # 314827</div>

    <p class="email">Email: braxo@braxoconstruction.example</p>

    <h1 class="contractor-name">Wendell Trusk contractor</h1>

    <div class="phones">
      <div class="row"><span class="label">Mobile:</span><span>(415) 555-0147</span></div>
      <div class="row"><span class="label">Phone:</span><span>(650) 555-0182</span></div>
      <div class="row"><span class="label">Fax:</span><span>(650) 555-0183</span></div>
    </div>

    <address class="address" style="font-style: normal;">
      4158 Garnet Row,<br>
      San Bruno, California 94066
    </address>
  </main>
</body>
</html>
```